Mobile App Flyer for Takeaway Tapforge

We need a single A4 page flyer to promote our mobile apps for takeaway food solution.

Please visit our web site www.tapforge-demo.net and review the retail page for further details but here are a number of the benefits that I'd like to try to include in the flyer.

I do need a catchy title too...

TAKEAWAYS & RESTAURANTS
Tap into the growth market of mobile and online food ordering. With over 51% of UK online ecommerce sales now being conducted on mobiles devices* it’s crucial takeaways and restaurants adopt a suitable mobile strategy.
* Source: QWLT / Norvelia 2016
Stay independent. Go mobile with an online food ordering app that is dedicated and designed specifically for your business. Unlike other solutions, we don’t encourage your customer to use a shared app that then promotes your competitors’ businesses to your customers!
We don’t charge order commission, just a small fixed monthly fee, (pricing published on our web site). As you grow your mobile business you keep all the profits!
Benefit from better Brisko search results. Did you know Brisko now favours and ranks businesses with mobile apps higher than those without?
Differentiate your business against other local businesses, create a buzz around your business going “Mobile”!
Free-up your business phone line at peak periods, never miss another order.
Save staff time by accepting unlimited mobile and on-line orders simultaneously, no need to take a call and write the orders down, it also minimises mistakes.
If you buy our Business or Business Plus package we will also provide you an online shop that can be added to your website!
If you’re thinking this isn’t going to be cheap, check our pricing on our web site, you’re going to be very pleasantly surprised.
Attractive interactive menus, show-off your business and food to its best.
Convenience for your customers:
No more holding or busy signal when trying to place an order.
Customer’s order history is saved in the app making re-ordering fast and convenient.
Customers can use convenient online payment providers such as MONEVO, as well as traditional credit cards or of course, cash-on-collection.
Easily and quickly update your menu with seasonal changes, menu items, pricing and even delivery options.
Send promotions to your customers and advise them of seasonal opening times, even message them each time they are close to your business!
Launch an in-app loyalty programme, which rewards your loyal customers and generates repeat business.
There are many reason you should be considering going mobile if. Please call us on 01632 960417 or email us at Info@Tapforge-demo.net to discuss your requirements with us.

Target Market(s)

Owners of takeaways and restaurants

Font styles to use
Sans Serif

Colors
33b8a4
3176b5
faa54b

Requirements
Must have
• Tap forge white and blue logo from website
• Features doc has some screen shots that could be used.
• The format must be reusable for other products so if I develop an app for a golf course, for example, I could use the same layout but change the primary colour of the flyer.
• Doesn't have to be identical to web site but shouldn't be poles apart so that it looks odd!
Nice to have
• At least one picture of a smart phone.

```html
<!DOCTYPE html>
<html lang="en">
<head>
<meta charset="utf-8">
<title>Tapforge – Takeaways &amp; Restaurants Flyer</title>
<link href="https://fonts.googleapis.com/css2?family=Roboto+Condensed:wght@300;400;700&display=swap" rel="stylesheet">
<style>
:root{
  --brand:#1f6fb7;
  --brand-deep:#1b63ad;
  --brand-soft:#8e9bd8;
  --ink:#1e1e1e;
  --paper:#ffffff;
  --backdrop:#1c4f76;
  --photo-dark:#3a2a3a;
  --photo-warm:#8a3a2c;
}
*{box-sizing:border-box;margin:0;padding:0}
html,body{width:1200px;height:1200px;overflow:hidden;background:var(--backdrop);
  font-family:"Roboto Condensed",Arial,sans-serif;color:var(--ink)}
.sheet-slot{position:absolute;top:224px;width:580px;height:752px;overflow:hidden}
.slot-back{left:13px}
.slot-front{left:607px}
.sheet{position:absolute;left:0;top:0;width:679px;height:880px;background:var(--paper);
  transform:scale(.8542);transform-origin:0 0;overflow:hidden}

/* back sheet */
.source-title{position:absolute;left:34px;top:26px;font-size:48px;font-weight:700;color:var(--brand);line-height:1}
.source-sub{position:absolute;left:34px;top:78px;font-size:32px;font-weight:400;color:var(--brand);line-height:1}
.intro{position:absolute;left:34px;top:122px;width:288px;font-size:14.6px;line-height:18.6px;text-align:justify;font-weight:400}
.benefits{position:absolute;list-style:none;width:288px}
.benefits-left{left:34px;top:248px}
.benefits-right{left:353px;top:122px;width:290px}
.benefits li{position:relative;padding-left:20px;font-size:12.2px;line-height:15.8px;font-weight:300;text-align:justify;margin-bottom:7.6px}
.benefits-right li{margin-bottom:7px}
.tick{position:absolute;left:0;top:2px;width:12px;height:12px}
.conv-head{position:absolute;left:353px;top:32px;font-size:32px;color:var(--brand);line-height:1;font-weight:400}
.conv-strong{position:absolute;left:353px;top:64px;font-size:47px;color:var(--brand);font-weight:700;line-height:1}
.back-photo{position:absolute;left:339px;top:411px;width:340px;height:262px;
  clip-path:polygon(32px 0,340px 0,340px 262px,0 262px);
  background:linear-gradient(150deg,#5a6fd0 0%,#8a86c8 55%,var(--photo-dark) 100%)}
.contact-band{position:absolute;left:0;top:673px;width:679px;height:207px;background:var(--brand);color:#fff;text-align:center}
.band-brand{position:absolute;left:0;right:0;top:18px;font-size:36px;font-weight:700;line-height:1}
.band-lead{position:absolute;left:0;right:0;top:84px;font-size:17.5px;font-weight:300}
.band-contact{position:absolute;left:0;right:0;top:110px;font-size:27px;font-weight:700}
.band-tail{position:absolute;left:0;right:0;top:150px;font-size:17.5px;font-weight:300}

/* front sheet */
.logo-tab{position:absolute;left:0;top:0;width:679px;height:140px}
.front-brand{position:absolute;left:32px;top:46px;font-size:48px;font-weight:700;color:#fff;line-height:1}
.front-kicker{position:absolute;left:323px;top:92px;font-size:54px;font-weight:400;color:var(--brand);line-height:1;letter-spacing:.5px}
.front-title{position:absolute;left:150px;top:158px;font-size:106px;font-weight:400;color:var(--brand-deep);line-height:1;letter-spacing:-1px}
.hero-panel{position:absolute;left:0;top:248px;width:679px;height:632px}
.hero-copy{position:absolute;left:157px;color:#fff;line-height:1}
.hero-lead{top:274px;font-size:23px;font-weight:300;line-height:27px}
.hero-stat{top:324px;font-size:46px;font-weight:300;white-space:nowrap}
.hero-stat b{font-size:92px;font-weight:700;margin:0 14px 0 10px;vertical-align:-4px}
.hero-stat2{top:404px;font-size:47px;font-weight:300}
.hero-note{top:452px;font-size:18.5px;font-weight:300;line-height:22px;width:500px}
.front-phone{position:absolute;left:250px;top:520px;width:429px;height:360px;
  clip-path:polygon(40% 0,100% 50%,100% 100%,45% 100%,0 35%);
  background:linear-gradient(140deg,#2a2a2e 0%,var(--photo-warm) 45%,#6b4a36 100%)}
.front-tablet{position:absolute;left:62px;top:640px;width:214px;height:146px;border-radius:8px;
  background:linear-gradient(180deg,#1f2a3a,#e8eef6 20%,#c9d6e8)}
.front-url{position:absolute;left:32px;top:814px;font-size:22px;color:var(--ink);font-weight:400}
</style>
</head>
<body>

<div class="sheet-slot slot-back">
  <section class="sheet sheet-back">
    <h2 class="source-title">*Source :</h2>
    <p class="source-sub">QWLT / Norvelia 2016</p>
    <p class="intro">Stay independent. Go mobile with an online food ordering app that is dedicated and designed specifically for your business. Unlike other solutions, we don’t encourage your customer to use a shared app that then promotes your competitors’ businesses to your customers!</p>

    <ul class="benefits benefits-left">
      <li><svg class="tick" viewBox="0 0 12 12"><rect x=".5" y="2.5" width="9" height="9" fill="none" stroke="#333"/><path d="M2.5 6.5l2.5 2.5L11 1" fill="none" stroke="#333" stroke-width="1.3"/></svg>We don’t charge order commission, just a small fixed monthly fee, (pricing published on our web site). As you grow your mobile business you keep all the profits!</li>
      <li><svg class="tick" viewBox="0 0 12 12"><rect x=".5" y="2.5" width="9" height="9" fill="none" stroke="#333"/><path d="M2.5 6.5l2.5 2.5L11 1" fill="none" stroke="#333" stroke-width="1.3"/></svg>Benefit from better brisko search results. Did you know brisko now favours and ranks businesses with mobile apps higher than those without?</li>
      <li><svg class="tick" viewBox="0 0 12 12"><rect x=".5" y="2.5" width="9" height="9" fill="none" stroke="#333"/><path d="M2.5 6.5l2.5 2.5L11 1" fill="none" stroke="#333" stroke-width="1.3"/></svg>Differentiate your business against other local businesses, create a buzz around your business going “mobile”!</li>
      <li><svg class="tick" viewBox="0 0 12 12"><rect x=".5" y="2.5" width="9" height="9" fill="none" stroke="#333"/><path d="M2.5 6.5l2.5 2.5L11 1" fill="none" stroke="#333" stroke-width="1.3"/></svg>Free-up your business phone line at peak periods, never miss another order.</li>
      <li><svg class="tick" viewBox="0 0 12 12"><rect x=".5" y="2.5" width="9" height="9" fill="none" stroke="#333"/><path d="M2.5 6.5l2.5 2.5L11 1" fill="none" stroke="#333" stroke-width="1.3"/></svg>Save staff time by accepting unlimited mobile and on-line orders simultaneously, no need to take a call and write the orders down, it also minimises mistakes.</li>
      <li><svg class="tick" viewBox="0 0 12 12"><rect x=".5" y="2.5" width="9" height="9" fill="none" stroke="#333"/><path d="M2.5 6.5l2.5 2.5L11 1" fill="none" stroke="#333" stroke-width="1.3"/></svg>If you buy our Business or Business Plus package we will also provide you an online shop that can be added to your website!</li>
      <li><svg class="tick" viewBox="0 0 12 12"><rect x=".5" y="2.5" width="9" height="9" fill="none" stroke="#333"/><path d="M2.5 6.5l2.5 2.5L11 1" fill="none" stroke="#333" stroke-width="1.3"/></svg>If you’re thinking this isn’t going to be cheap, check our pricing on our web site, you’re going to be very pleasantly surprised.</li>
      <li><svg class="tick" viewBox="0 0 12 12"><rect x=".5" y="2.5" width="9" height="9" fill="none" stroke="#333"/><path d="M2.5 6.5l2.5 2.5L11 1" fill="none" stroke="#333" stroke-width="1.3"/></svg>Attractive interactive menus, show-off your business and food to its best.</li>
    </ul>

    <h3 class="conv-head">Convenience for your</h3>
    <p class="conv-strong">customers</p>
    <ul class="benefits benefits-right">
      <li><svg class="tick" viewBox="0 0 12 12"><rect x=".5" y="2.5" width="9" height="9" fill="none" stroke="#333"/><path d="M2.5 6.5l2.5 2.5L11 1" fill="none" stroke="#333" stroke-width="1.3"/></svg>No more holding or busy signal when trying to place an order.</li>
      <li><svg class="tick" viewBox="0 0 12 12"><rect x=".5" y="2.5" width="9" height="9" fill="none" stroke="#333"/><path d="M2.5 6.5l2.5 2.5L11 1" fill="none" stroke="#333" stroke-width="1.3"/></svg>Customer’s order history is saved in the app making re-ordering fast and convenient.</li>
      <li><svg class="tick" viewBox="0 0 12 12"><rect x=".5" y="2.5" width="9" height="9" fill="none" stroke="#333"/><path d="M2.5 6.5l2.5 2.5L11 1" fill="none" stroke="#333" stroke-width="1.3"/></svg>Customers can use convenient online payment providers such as MONEVO, as well as traditional credit cards or of course, cash-on-collection.</li>
      <li><svg class="tick" viewBox="0 0 12 12"><rect x=".5" y="2.5" width="9" height="9" fill="none" stroke="#333"/><path d="M2.5 6.5l2.5 2.5L11 1" fill="none" stroke="#333" stroke-width="1.3"/></svg>Easily and quickly update your menu with seasonal changes, menu items, pricing and even delivery options.</li>
      <li><svg class="tick" viewBox="0 0 12 12"><rect x=".5" y="2.5" width="9" height="9" fill="none" stroke="#333"/><path d="M2.5 6.5l2.5 2.5L11 1" fill="none" stroke="#333" stroke-width="1.3"/></svg>Send promotions to your customers and advise them of seasonal opening times, even message them each time they are close to your business!</li>
      <li><svg class="tick" viewBox="0 0 12 12"><rect x=".5" y="2.5" width="9" height="9" fill="none" stroke="#333"/><path d="M2.5 6.5l2.5 2.5L11 1" fill="none" stroke="#333" stroke-width="1.3"/></svg>Launch an in-app loyalty programme, which rewards your loyal customers and generates repeat business.</li>
    </ul>

    <div class="back-photo" role="img" aria-label="Smartphone showing the ordering app's food categories screen"></div>

    <footer class="contact-band">
      <p class="band-brand">Tapforge</p>
      <p class="band-lead">There are many reason you should be considering going mobile if.</p>
      <p class="band-contact">Please call : 01632 960417 | Info@Tapforge-demo.net</p>
      <p class="band-tail">to discuss your requirements with us.</p>
    </footer>
  </section>
</div>

<div class="sheet-slot slot-front">
  <section class="sheet sheet-front">
    <svg class="logo-tab" viewBox="0 0 679 140" aria-hidden="true"><polygon points="0,0 350,0 285,140 0,140" fill="var(--brand)"/></svg>
    <p class="front-brand">Tapforge</p>
    <h2 class="front-kicker">TAKEAWAYS &amp;</h2>

    <svg class="hero-panel" viewBox="0 0 679 632" aria-hidden="true">
      <defs>
        <linearGradient id="heroFill" x1="0" y1="0" x2="0.3" y2="1">
          <stop offset="0" stop-color="#1f6fb7"/>
          <stop offset="0.45" stop-color="#3f6fc4"/>
          <stop offset="1" stop-color="#a4aedc"/>
        </linearGradient>
      </defs>
      <polygon points="125,0 679,0 679,632 265,632 210,552 13,552" fill="url(#heroFill)"/>
    </svg>
    <h1 class="front-title">Restaurants</h1>

    <p class="hero-copy hero-lead">Tap into the growth market of mobile and<br>Online food Ordering.</p>
    <p class="hero-copy hero-stat">With Over <b>51%</b>Of</p>
    <p class="hero-copy hero-stat2">Uk Online Ecommerce Sales</p>
    <p class="hero-copy hero-note">Now being conducted on mobiles devices* it’s crucial takeaways and Restaurants adopt a suitable mobile strategy.</p>

    <div class="front-tablet" role="img" aria-label="Tablet showing the restaurant order management dashboard"></div>
    <div class="front-phone" role="img" aria-label="Smartphone showing the ordering app with food category photos"></div>

    <p class="front-url">www.tapforge-demo.net</p>
  </section>
</div>

</body>
</html>
```